Crooked Falcon Ale House & Sports Grill Menu

This is my dine in menu for my sports bar. I would like it to be playful and fun. The colors of my logo are also the colors of my bar. You can look at facebook or crookedfalconalehouse.example to see pictures. My current menu is a trifold and I would like to move away from that design. I like a the menu to flow, but am very open to new concepts. I feel like my current one is too boring and not professional enough as well as not catchy. I like a colored page, with colored lettering not necessarily black or white text. I currently use the colors of my log on my menu but like the idea of something that is not boring.

Target Market(s)

customers coming into my bar

Industry/Entity Type

Sports Bar

Requirements
Must have
• LOGO, Specials,
Nice to have
• pictures of food
Should not have
• open to all designs

```html
<!DOCTYPE html>
<html lang="en">
<head>
<meta charset="utf-8">
<title>Crooked Falcon Ale House &amp; Sports Grill Menu</title>
<link href="https://fonts.googleapis.com/css2?family=Open+Sans:wght@600;700;800&display=swap" rel="stylesheet">
<style>
  :root {
    --ink: #0d0c0b;
    --board: #1e1c1a;
    --gold: #d9922a;
    --gold-line: #c9923a;
    --text: #ffffff;
    --plank-light: #f0a73a;
    --plank-dark: #c8761c;
  }
  * { margin: 0; padding: 0; box-sizing: border-box; }
  html, body { width: 1200px; height: 933px; overflow: hidden; }
  body {
    position: relative;
    font-family: "Open Sans", Arial, sans-serif;
    color: var(--text);
    background: linear-gradient(180deg, var(--ink) 0%, #161513 55%, var(--board) 100%);
  }
  .board-grain {
    position: absolute; inset: 0;
    background: repeating-linear-gradient(90deg, rgba(255,255,255,0.025) 0 2px, transparent 2px 95px);
  }
  .floor { position: absolute; left: 0; top: 0; width: 1200px; height: 933px; }
  .frame { position: absolute; top: 0; left: 0; width: 1200px; height: 933px; }
  .panel { position: absolute; width: 420px; }
  .panel--left { left: 98px; }
  .panel--right { left: 698px; }
  .section-title {
    position: absolute;
    font-size: 31px; font-weight: 700; color: var(--gold);
    letter-spacing: 0.2px; line-height: 1;
  }
  .copy {
    position: absolute; width: 400px;
    font-size: 9.9px; font-weight: 700; line-height: 14px; text-transform: uppercase;
  }
  .item-name {
    position: absolute;
    font-size: 12.4px; font-weight: 700; color: var(--gold); text-transform: uppercase; line-height: 1;
    white-space: nowrap;
  }
  .item-name small { font-size: 9.9px; color: var(--text); }
  .photo {
    position: absolute; border-radius: 50%;
    border: 2px solid #2b2926;
  }
  .photo--sandwich {
    left: 459px; top: 503px; width: 130px; height: 130px;
    background: radial-gradient(circle at 45% 45%, #c9c2a8 0%, #9c8f6a 45%, #4f4a3a 100%);
  }
  .photo--wings {
    left: 998px; top: 490px; width: 160px; height: 160px;
    background: radial-gradient(circle at 50% 45%, #c25a2a 0%, #b7a79b 50%, #8f8a86 100%);
  }
</style>
</head>
<body>
  <div class="board-grain"></div>

  <svg class="floor" viewBox="0 0 1200 933" aria-hidden="true">
    <defs>
      <linearGradient id="plank" x1="0" y1="0" x2="0" y2="1">
        <stop offset="0" stop-color="#c8761c"/>
        <stop offset="0.35" stop-color="#f0a73a"/>
        <stop offset="1" stop-color="#c8761c"/>
      </linearGradient>
    </defs>
    <polygon points="0,815 1200,763 1200,933 0,933" fill="url(#plank)"/>
    <g stroke="#b3651a" stroke-width="3" opacity="0.5">
      <line x1="0" y1="850" x2="1200" y2="820"/>
      <line x1="0" y1="880" x2="1200" y2="860"/>
      <line x1="0" y1="905" x2="1200" y2="895"/>
    </g>
  </svg>

  <svg class="frame" viewBox="0 0 1200 933" aria-hidden="true" fill="none" stroke="#c9923a" stroke-width="2.5">
    <path d="M92,62 H510 A30,30 0 0 0 540,92 V755 A30,30 0 0 0 510,785 H92 A30,30 0 0 0 62,755 V92 A30,30 0 0 0 92,62 Z"/>
    <path d="M692,62 H1108 A30,30 0 0 0 1138,92 V755 A30,30 0 0 0 1108,785 H692 A30,30 0 0 0 662,755 V92 A30,30 0 0 0 692,62 Z"/>
  </svg>

  <section class="panel panel--left">
    <h2 class="section-title" style="top:95px">CHEESESTEAKS</h2>
    <p class="copy" style="top:138px">Made with shaved ribeye on the world famous Marabella roll. Comes with fries or chips, add whatever toppings you want: pepper relish, mushrooms, bell peppers, pepperoncinis, jalapenos, marinara, or hogie style (lettuce, tomato, &amp; mayo) – .75ea</p>
    <h3 class="item-name" style="top:212px">Famous Philly</h3>
    <p class="copy" style="top:227px">Shaved steak, grilled onions &amp; white american cheese, provolone, or cheese sauce – 10.95</p>
    <h3 class="item-name" style="top:273px">Chicken Philly</h3>
    <p class="copy" style="top:288px">Chopped chicken, grilled onions &amp; white american cheese, provolone, or cheese sauce – 10.95</p>

    <h2 class="section-title" style="top:372px">SANDWICHES</h2>
    <p class="copy" style="top:412px">All sandwiches come on a sub roll &amp; served with fries or chips</p>
    <h3 class="item-name" style="top:444px">Italian Sausage</h3>
    <p class="copy" style="top:459px">½ pound of sausage covered with onions and bell peppers on a hogie roll. You can’t resist my italian sausage!!! – 10.95</p>
    <h3 class="item-name" style="top:505px">Bacon &amp; Jalapeno Grilled Cheese</h3>
    <p class="copy" style="top:520px">Half pound of bacon (6 slices) – 10.95</p>
    <h3 class="item-name" style="top:551px">Buffalo Ranch Chicken Sandwich</h3>
    <p class="copy" style="top:566px">Ranch and medium sauce on a breaded chicken breast – 10.95</p>
    <h3 class="item-name" style="top:598px">Grilled Chicken Sandwich (8 oz) <small>– 10.95</small></h3>
    <h3 class="item-name" style="top:629px">Gyro</h3>
    <p class="copy" style="top:644px">Gyro meat on the best pita bread you’ll ever have. The meat is smoth-<br>ered in our soon to be famous tzatziki sauce. – 10.95</p>
    <h3 class="item-name" style="top:690px">Falcon Dog</h3>
    <p class="copy" style="top:705px">This is our version of a coney dog. A deep fried beef frank on an Marabella roll topped with our guy Marty’s coney meat sauce, shredded cheddar, raw onions, pepperoncinis, &amp; jalapenos.</p>
  </section>

  <div class="photo photo--sandwich" role="img" aria-label="Photo of a gyro sandwich with onions and chips"></div>

  <section class="panel panel--right">
    <h2 class="section-title" style="top:95px">FALCON STYLE</h2>
    <p class="copy" style="top:138px">(The fries come on the sub, not on the side!!)</p>
    <p class="copy" style="top:167px">&nbsp;&nbsp;These subs come on a hogie roll that is not toasted. The meat is thrown on the grill for a minute to heat it up a little and then they are covered with french fries, provolone cheese, and our soon to be famous pepper relish coleslaw. It’s a one of a kind taste with a little kick!</p>
    <h3 class="item-name" style="top:255px">Pastrami</h3>
    <p class="copy" style="top:270px">Our premium pastrami is shipped in from back east! You’re going to love it!!!. – 11.95</p>
    <h3 class="item-name" style="top:316px">Prime Rib</h3>
    <p class="copy" style="top:331px">Shaved prime rib that will melt in your mouth. – 13.95</p>
    <h3 class="item-name" style="top:362px">Roast Beef</h3>
    <p class="copy" style="top:377px">A very high quality roast beef. – 11.95</p>

    <h2 class="section-title" style="top:425px">JUMBO WINGS</h2>
    <p class="copy" style="top:467px">Add a side of fries or chips with wings – 2.00<br>Finally wings with some meat on them!!!!<br>Wings are jointed wings, a flat and drumstick together.</p>
    <h3 class="item-name" style="top:528px">Jumbo Traditional Wings</h3>
    <p class="copy" style="top:543px">3 jointed wings (3 flats &amp; 3 drums) – 8.95<br>6 jointed wings (6 flats &amp; 6 drums) – 16.95</p>
    <h3 class="item-name" style="top:588px">Boneless Wings</h3>
    <p class="copy" style="top:603px">12 wings – 8.95<br>24 wings – 17.95</p>
    <h3 class="item-name" style="top:650px">Chicken Tender (4) Basket w/Fries or Chips <small>– 12.95</small></h3>
    <p class="copy" style="top:677px">Sauce choices<br>Bourbon BBQ, medium, thai zing, mango habanero,<br>hot (with jalapeno), scorchin’ (with habanero peppers), Falcon<br>punch (with ghost peppers)</p>
  </section>

  <div class="photo photo--wings" role="img" aria-label="Photo of jumbo chicken wings on a paper plate"></div>
</body>
</html>
```